Life Coach for Lawyers Business Card Design

Elegant, original, business card design for life coaching service for associate attorneys who work in big law and struggle with stress, overwhelm, and time management. Double sided design.

Target Market(s)

Women associate attorneys who work in big law and struggle with stress, overwhelm, and time management.

Industry/Entity Type

Life Coaching

Contact Information for Business Card

Marissa Pendrell
Life Coach
518.677.3941
calmbriefcounsel.net
marissa@calmbriefcounsel.net
@calmbriefcounsel (Instagram)

Font styles to use
Other font styles liked:
• Silver South font duo. See uploaded files.

Requirements
Must have
• Icons for phone, website, email, and Instagram instead of words. Specific colors used in my logo (171B2B, 421121, FFFFFF)
Nice to have
• Foil. Embossed. Feminine design.
Should not have
• Any colors other than those used in logo. See uploaded files.

```html
<!DOCTYPE html>
<html lang="en">
<head>
<meta charset="utf-8">
<title>Calm Brief Counsel — Business Card</title>
<link rel="stylesheet" href="https://fonts.googleapis.com/css2?family=Bodoni+Moda:wght@400;500&display=swap">
<style>
  :root {
    --backdrop: #5f5f62;
    --card: #141416;
    --silver: #d8d5d8;
    --rose: #8e5f6b;
    --rose-light: #b9959e;
    --icon-tile: #f2f0f1;
    --icon-ink: #421121;
  }
  html, body {
    margin: 0;
    padding: 0;
    width: 1200px;
    height: 1200px;
    overflow: hidden;
    background: var(--backdrop);
  }
  .canvas {
    position: relative;
    width: 1200px;
    height: 1200px;
    font-family: "Bodoni Moda", "Didot", serif;
  }
  .card {
    position: absolute;
    left: 182px;
    width: 837px;
    height: 475px;
    background: var(--card);
    box-shadow: 0 10px 18px rgba(0,0,0,0.45);
  }
  .card--front { top: 105px; }
  .card--back { top: 615px; }

  .brand {
    position: absolute;
    left: 0;
    right: 0;
    text-align: center;
    color: var(--silver);
    font-weight: 400;
    letter-spacing: 0.06em;
    text-transform: uppercase;
    line-height: 1;
  }
  .card--front .brand { top: 200px; font-size: 58px; }
  .card--back .brand { top: 90px; font-size: 52px; }

  .holder {
    position: absolute;
    left: 60px;
    top: 345px;
    color: var(--rose);
  }
  .holder__name {
    font-size: 31px;
    font-weight: 500;
    margin: 0;
    line-height: 1.1;
  }
  .holder__role {
    font-size: 23px;
    margin: 6px 0 0;
    line-height: 1.1;
  }

  .contacts {
    position: absolute;
    left: 380px;
    top: 296px;
    margin: 0;
    padding: 0;
    list-style: none;
  }
  .contacts__item {
    display: flex;
    align-items: center;
    height: 38px;
    color: var(--rose-light);
    font-size: 19px;
    letter-spacing: 0.03em;
  }
  .contacts__icon {
    width: 25px;
    height: 25px;
    margin-right: 16px;
    flex: none;
  }
</style>
</head>
<body>
<main class="canvas">

  <section class="card card--front" aria-label="Card front">
    <p class="brand">Calm Brief Counsel</p>
  </section>

  <section class="card card--back" aria-label="Card back">
    <p class="brand">Calm Brief Counsel</p>

    <div class="holder">
      <p class="holder__name">Marissa Pendrell</p>
      <p class="holder__role">Life Coach</p>
    </div>

    <ul class="contacts">
      <li class="contacts__item">
        <svg class="contacts__icon" viewBox="0 0 24 24" aria-hidden="true">
          <rect width="24" height="24" fill="var(--icon-tile)"/>
          <path d="M8 5l2.5 0 1 3.5-1.6 1.2c.8 1.7 2.2 3.1 3.9 3.9l1.2-1.6 3.5 1v2.5c0 .8-.7 1.5-1.5 1.5C10.6 17 7 13.4 7 6.5 7 5.7 7.4 5 8 5z" fill="var(--icon-ink)"/>
        </svg>
        518.677.3941
      </li>
      <li class="contacts__item">
        <svg class="contacts__icon" viewBox="0 0 24 24" aria-hidden="true">
          <rect width="24" height="24" fill="var(--icon-tile)"/>
          <g fill="none" stroke="var(--icon-ink)" stroke-width="1.2">
            <circle cx="12" cy="12" r="6.5"/>
            <ellipse cx="12" cy="12" rx="3" ry="6.5"/>
            <line x1="5.5" y1="12" x2="18.5" y2="12"/>
          </g>
        </svg>
        calmbriefcounsel.net
      </li>
      <li class="contacts__item">
        <svg class="contacts__icon" viewBox="0 0 24 24" aria-hidden="true">
          <rect width="24" height="24" fill="var(--icon-tile)"/>
          <rect x="5" y="7" width="14" height="10" fill="var(--icon-ink)"/>
          <path d="M5 7l7 5.5L19 7" fill="none" stroke="var(--icon-tile)" stroke-width="1.2"/>
        </svg>
        marissa@calmbriefcounsel.net
      </li>
      <li class="contacts__item">
        <svg class="contacts__icon" viewBox="0 0 24 24" aria-hidden="true">
          <rect width="24" height="24" fill="var(--icon-tile)"/>
          <rect x="7" y="7" width="10" height="10" fill="none" stroke="var(--icon-ink)" stroke-width="1.3"/>
        </svg>
        @calmbriefcounsel
      </li>
    </ul>
  </section>

</main>
</body>
</html>
```